WRM Marketing Postcard

Design a 2 Sided marketing postcard for our Real estate management caompany. Looking for a professional yet fresh look that will be printed on a 6"x9" glossy flier

Contact information is www.wexleymanagement.com wexleymanagement@inboxvane.com and 312-555-0187

WE are targeting small condo and town home properties to take on their administrative responsibilities of management

```html
<!DOCTYPE html>
<html lang="en">
<head>
<meta charset="utf-8">
<title>WRM Marketing Postcard</title>
<link href="https://fonts.googleapis.com/css2?family=Cinzel:wght@600;700&family=Montserrat:wght@400;600;700&display=swap" rel="stylesheet">
<style>
  :root {
    --gold: #d9a02a;
    --gold-deep: #c98f1b;
    --navy: #1f4fa0;
    --charcoal: #2b2b2d;
    --ink: #262626;
    --white: #ffffff;
    --page: #eceff1;
  }
  * { box-sizing: border-box; margin: 0; padding: 0; }
  html, body { width: 947px; height: 1200px; overflow: hidden; }
  body { background: var(--page); font-family: "Montserrat", sans-serif; position: relative; }
  .card { position: absolute; left: 90px; width: 768px; height: 518px; background: var(--white); overflow: hidden; box-shadow: 0 2px 8px rgba(0,0,0,.15); }
  .front { top: 60px; }
  .back { top: 636px; }
  .abs { position: absolute; }

  .brand { font-weight: 700; color: var(--gold-deep); text-align: center; line-height: 1; }
  .brand .name { font-size: 40px; letter-spacing: 2px; display: block; }
  .brand .sub { font-size: 9px; letter-spacing: 1px; display: block; margin-top: 5px; }

  .tagline { right: 23px; top: 38px; text-align: right; font-weight: 700; font-size: 16px; line-height: 19px; color: var(--ink); }
  .rule-gold { left: 0; top: 96px; width: 768px; height: 5px; background: var(--gold); }

  .photo-building { left: 300px; top: 101px; width: 468px; height: 359px; background: linear-gradient(180deg, #9fb2c6 0%, #e9eaea 18%, #d7d9da 45%, #8d8f91 70%, #6d6f71 100%); }
  .sky-panel { left: 0; top: 101px; width: 330px; height: 385px; background: linear-gradient(160deg, #2c62b4 0%, var(--navy) 55%, #1c4891 100%); clip-path: polygon(0 0, 100% 0, 98% 100%, 0 100%); }

  .heading { font-family: "Cinzel", serif; font-weight: 700; color: var(--gold); font-size: 16px; letter-spacing: .5px; line-height: 18px; }
  .item { font-size: 10.2px; line-height: 12.4px; }
  .item.light { color: var(--white); }
  .item.dark { color: #333; }
  .tick { padding-left: 15px; }
  .tick::before { content: ""; position: absolute; left: 2px; top: 1px; width: 3px; height: 7px; border-right: 1.3px solid var(--gold); border-bottom: 1.3px solid var(--gold); transform: rotate(40deg); }
  .tick.white::before { border-color: rgba(255,255,255,.8); }

  .icon-badge { width: 38px; height: 38px; border-radius: 50%; background: var(--gold); display: flex; align-items: center; justify-content: center; }

  .work-box { left: 374px; top: 146px; width: 320px; height: 314px; background: rgba(255,255,255,.88); }

  .phone-band { left: 0; top: 460px; width: 330px; height: 58px; background: var(--gold); clip-path: polygon(0 0, 100% 0, 93% 100%, 0 100%); }
  .contact-band { left: 310px; top: 460px; width: 458px; height: 58px; background: var(--charcoal); border-top: 3px solid var(--gold); clip-path: polygon(6% 0, 100% 0, 100% 100%, 0 100%); }
  .phone { left: 36px; top: 468px; display: flex; align-items: center; gap: 10px; font-family: "Cinzel", serif; font-weight: 600; font-size: 32px; line-height: 40px; color: var(--white); }
  .contact { top: 482px; display: flex; align-items: center; gap: 7px; color: var(--white); font-size: 10.5px; }
  .divider { left: 526px; top: 478px; width: 1px; height: 22px; background: #555; }

  .back-head { left: 0; top: 0; width: 337px; height: 98px; background: var(--charcoal); }
  .back-list { left: 0; top: 98px; width: 337px; height: 282px; background: var(--gold); }
  .photo-house { left: 0; top: 380px; width: 337px; height: 138px; background: linear-gradient(160deg, #f4f5f6 0%, #dfe2e5 50%, #4a5058 100%); }
  .stamp { left: 645px; top: 40px; width: 84px; height: 104px; border: 1px solid #555; }
</style>
</head>
<body>

<section class="card front">
  <div class="abs brand" style="left:38px;top:34px;width:200px;">
    <span class="name">WEXLEY</span>
    <span class="sub">PROPERTY MANAGEMENT LLC</span>
  </div>
  <p class="abs tagline">Improve compliance, reporting, and communication<br>amongst all owners and board members</p>
  <div class="abs rule-gold"></div>

  <div class="abs photo-building" role="img" aria-label="Photo of a modern white residential building with balconies against a blue sky"></div>
  <div class="abs sky-panel" role="img" aria-label="Blue sky with soft clouds"></div>

  <h2 class="abs heading" style="left:37px;top:117px;">Who we are?</h2>

  <div class="abs icon-badge" style="left:33px;top:147px;">
    <svg width="20" height="16" viewBox="0 0 20 16"><rect x="1" y="4" width="18" height="11" rx="1.5" fill="none" stroke="#fff" stroke-width="1.5"/><path d="M7 4V2h6v2M1 8h18" fill="none" stroke="#fff" stroke-width="1.5"/></svg>
  </div>
  <p class="abs item light" style="left:81px;top:154px;width:245px;">A professional services organization with a focus on small (3-10 unit) residential buildings</p>

  <div class="abs icon-badge" style="left:33px;top:191px;">
    <svg width="18" height="22" viewBox="0 0 18 22"><circle cx="9" cy="8" r="6.5" fill="none" stroke="#fff" stroke-width="1.5"/><circle cx="9" cy="8" r="3" fill="#fff"/><path d="M5 13l-1 8 5-3 5 3-1-8" fill="none" stroke="#fff" stroke-width="1.5"/></svg>
  </div>
  <p class="abs item light" style="left:81px;top:198px;width:245px;">Over 30 years of combined experience in real estate and property management</p>

  <div class="abs icon-badge" style="left:33px;top:236px;">
    <svg width="22" height="16" viewBox="0 0 22 16"><circle cx="11" cy="4" r="3" fill="#fff"/><circle cx="4" cy="7" r="2.3" fill="#fff"/><circle cx="18" cy="7" r="2.3" fill="#fff"/><path d="M5 16c0-4 2.5-6 6-6s6 2 6 6zM0 16c0-3 1.5-5 4-5s3 1 3 1M22 16c0-3-1.5-5-4-5s-3 1-3 1" fill="#fff"/></svg>
  </div>
  <p class="abs item light" style="left:81px;top:243px;width:245px;">Professional, courteous, timely service that is technologically driven</p>

  <h2 class="abs heading" style="left:37px;top:292px;">Why use WRM?</h2>
  <p class="abs item light tick white" style="left:33px;top:316px;width:285px;">Owners are rarely suited to manage associations and the burden often falls unfairly on one or two individuals to do all the work</p>
  <p class="abs item light tick white" style="left:33px;top:366px;width:285px;">Low monthly fees tailored to your needs</p>
  <p class="abs item light tick white" style="left:33px;top:391px;width:285px;">The association's board of directors maintains control of all decision making</p>

  <div class="abs work-box"></div>
  <h2 class="abs heading" style="left:392px;top:160px;">What we do?</h2>
  <p class="abs item dark tick" style="left:389px;top:184px;width:300px;">Remove the administrative burden of managing small residential buildings</p>
  <p class="abs item dark tick" style="left:389px;top:221px;width:300px;">Utilize economies of scale to reduce expenses for all owners across a wide variety of service providers</p>
  <p class="abs item dark tick" style="left:389px;top:258px;width:300px;">Collect all assessments and pay all bills</p>
  <p class="abs item dark tick" style="left:389px;top:283px;width:300px;">Provide monthly accounting reconciliation and reporting</p>
  <p class="abs item dark tick" style="left:389px;top:320px;width:300px;">Provide access to WRM's client portal with a central repository of all association materials (bylaws, financials, meeting minutes, communications, etc)</p>
  <p class="abs item dark tick" style="left:389px;top:370px;width:300px;">Issue 1099s to all contractors as required by law</p>
  <p class="abs item dark tick" style="left:389px;top:395px;width:300px;">Prepare year-end financial statements</p>
  <p class="abs item dark tick" style="left:389px;top:420px;width:300px;">Lender and legal HOA documents for mortgage companies and sales</p>

  <div class="abs phone-band"></div>
  <div class="abs contact-band"></div>
  <div class="abs phone">
    <svg width="24" height="24" viewBox="0 0 24 24"><path fill="#fff" d="M6.6 10.8a15.1 15.1 0 0 0 6.6 6.6l2.2-2.2c.3-.3.7-.4 1-.2 1.1.4 2.3.6 3.6.6.6 0 1 .4 1 1V20c0 .6-.4 1-1 1A17 17 0 0 1 3 4c0-.6.4-1 1-1h3.5c.6 0 1 .4 1 1 0 1.3.2 2.5.6 3.6.1.3 0 .7-.2 1z"/></svg>
    <span>312-555-0187</span>
  </div>
  <div class="abs contact" style="left:331px;">
    <svg width="10" height="10" viewBox="0 0 10 10"><circle cx="5" cy="5" r="4.3" fill="none" stroke="#fff"/><path d="M.7 5h8.6M5 .7c-2.4 2.6-2.4 6 0 8.6M5 .7c2.4 2.6 2.4 6 0 8.6" fill="none" stroke="#fff" stroke-width=".8"/></svg>
    <span>www.wexleymanagement.com</span>
  </div>
  <div class="abs divider"></div>
  <div class="abs contact" style="left:540px;">
    <svg width="10" height="8" viewBox="0 0 10 8"><rect width="10" height="8" rx="1" fill="#fff"/><path d="M0 1l5 3.5L10 1" fill="none" stroke="#2b2b2d" stroke-width="1"/></svg>
    <span>wexleymanagement@inboxvane.com</span>
  </div>
</section>

<section class="card back">
  <div class="abs back-head"></div>
  <div class="abs brand" style="left:0;top:30px;width:337px;color:var(--gold);">
    <span class="name">WEXLEY</span>
    <span class="sub">PROPERTY MANAGEMENT LLC</span>
  </div>

  <div class="abs back-list"></div>
  <p class="abs item light tick white" style="left:33px;top:112px;width:285px;">Cost effective property management solution for 3-10 unit buildings</p>
  <p class="abs item light tick white" style="left:33px;top:149px;width:285px;">Prices starting as low as $100/month</p>
  <p class="abs item light tick white" style="left:33px;top:174px;width:285px;">Utilize our economies of scale to reduce costs across existing services (trash, insurance, maintenance, etc)</p>
  <p class="abs item light tick white" style="left:33px;top:224px;width:285px;">Eliminate the unfair burden placed on a few owners to do all the work while others free-ride</p>
  <p class="abs item light tick white" style="left:33px;top:261px;width:285px;">Improve communication amongst all owners and board members</p>
  <p class="abs item light tick white" style="left:33px;top:298px;width:285px;">The association's board of directors maintain all decision-making power</p>
  <p class="abs item light tick white" style="left:33px;top:336px;width:285px;">Utilize our vetted service providers for prompt job completion and fair pricing</p>

  <div class="abs photo-house" role="img" aria-label="Photo of white wooden house gables with dark roofs and a snowy sky"></div>
  <div class="abs stamp"></div>
</section>

</body>
</html>
```